Roadside building business signage for a holistic health clinic.

Replace signs as shown in the attached file. They are perforated stickers that go on the windows as shown. Looking for something that has our logo and says the name of the practice with logo (Fernbrook Health & Wellness) also boldly says Acupuncture, IV Vitamins, and Holistic Health.
Possibly our phone number as well 318-627-5194
Updates

Please don't use pink except the logo. Earthy, organic tone colors appreciated.

Need of eye catching window signage of a holistic clinic on a brick building. Pink, purple, sage green, white color. Logo is pink on a white background. Please don't overload with too much pink. Words to include are "Fernbrook Health and Wellness(name of business)", "Direct Primary Care", " Medical acupuncture", "IV Vitamin Therapy", "fernbrookcare-example.com","318-627-5194".

Target Market(s)

People will see in their cars passing by the building. Busy roadside so need to be visible while passing in fast speed.

Industry/Entity Type

Health & Wellness

Font styles to use
Sans Serif

Colors

Designer to choose colors to be used in the design.

Requirements
Must have
• On sign must have words Holistic Medicine, Medical Acupuncture, Direct Primary Care and IV vitamins.
Nice to have
• Simple, minimalistic, artistic yet has clear message. White, Black, Violet, Pink (logo), Dark green, Sage green.
Should not have
• Bold colors (red, yellow, blue), same tone colors. Blue waves on the current signage (uploaded file) must go.

```html
<!DOCTYPE html>
<html lang="en">
<head>
<meta charset="utf-8">
<title>Fernbrook Health &amp; Wellness — Window Signage Panels</title>
<link rel="stylesheet" href="https://fonts.googleapis.com/css2?family=Tinos:wght@400;700&family=Italianno&display=swap">
<style>
  :root {
    --canvas: #000000;
    --panel-white: #f7f7f9;
    --panel-sage: #9aa898;
    --sage-hill: #97a495;
    --forest: #0f4a3a;
    --ink: #1d1d1d;
    --pin-pink: #e0287a;
    --white: #ffffff;
  }
  * { box-sizing: border-box; margin: 0; padding: 0; }
  html, body { width: 1200px; height: 1177px; overflow: hidden; background: var(--canvas); }
  .signage-canvas { position: relative; width: 1200px; height: 1177px; background: var(--canvas); }
  .window-panel {
    position: absolute; top: 478px; width: 220px; height: 221px; overflow: hidden;
  }
  .panel-brand { left: 115px; background: var(--panel-white); }
  .panel-contact { left: 360px; background: var(--panel-sage); text-align: center; }
  .panel-services { left: 605px; background: var(--panel-white); }
  .panel-accent { left: 859px; background: var(--panel-white); }

  .brand-card {
    position: absolute; left: 16px; top: 42px; width: 188px; height: 124px;
    background: var(--white); display: flex; flex-direction: column;
    align-items: center; justify-content: center;
  }
  .brand-dot { width: 34px; height: 34px; border-radius: 50%; background: var(--pin-pink); margin-bottom: 10px; }
  .brand-name {
    font-family: "Tinos", serif; font-weight: 400; color: var(--forest);
    font-size: 27px; letter-spacing: 3px; line-height: 1; text-align: center;
  }
  .brand-sub {
    font-family: "Tinos", serif; font-weight: 400; color: var(--forest);
    font-size: 9px; letter-spacing: 2.4px; margin-top: 5px; text-align: center;
  }

  .contact-name {
    font-family: "Tinos", serif; font-weight: 400; font-size: 34px; color: var(--ink);
    margin-top: 36px; line-height: 1; letter-spacing: 0.5px;
  }
  .contact-tagline {
    font-family: "Italianno", cursive; font-size: 24px; color: var(--ink); line-height: 1.1;
  }
  .contact-pin { display: block; margin: 12px auto 10px; }
  .contact-phone {
    font-family: "Tinos", serif; font-weight: 700; font-size: 28px; color: var(--ink); line-height: 1;
  }

  .service-list { list-style: none; position: absolute; left: 10px; top: 16px; }
  .service-item {
    position: relative; padding-left: 16px; margin-bottom: 14px;
    font-family: "Tinos", serif; font-size: 15px; line-height: 1.3; color: var(--ink);
    text-transform: uppercase;
  }
  .service-item::before {
    content: ""; position: absolute; left: 0; top: 5px; width: 9px; height: 9px;
    border-radius: 50%; background: var(--sage-hill);
  }
  .web-address {
    position: absolute; left: 0; right: 0; top: 130px; text-align: center;
    font-family: "Tinos", serif; font-size: 14px; color: var(--forest);
  }
  .hill { position: absolute; left: 0; bottom: 0; width: 220px; height: 221px; }
</style>
</head>
<body>
<main class="signage-canvas">
  <section class="window-panel panel-brand">
    <div class="brand-card">
      <span class="brand-dot"></span>
      <p class="brand-name">FERNBROOK</p>
      <p class="brand-sub">HEALTH &amp; WELLNESS</p>
    </div>
  </section>

  <section class="window-panel panel-contact">
    <h1 class="contact-name">FERNBROOK</h1>
    <p class="contact-tagline">Health and Wellness</p>
    <svg class="contact-pin" width="36" height="36" viewBox="0 0 40 40" aria-hidden="true">
      <circle cx="20" cy="20" r="20" fill="var(--pin-pink)"/>
      <path d="M20 9c-4.4 0-7.5 3.2-7.5 7.3 0 5.3 7.5 13.7 7.5 13.7s7.5-8.4 7.5-13.7C27.5 12.2 24.4 9 20 9z" fill="var(--white)"/>
      <circle cx="20" cy="16.5" r="3" fill="var(--pin-pink)"/>
    </svg>
    <p class="contact-phone">318-627-5194</p>
  </section>

  <section class="window-panel panel-services">
    <ul class="service-list">
      <li class="service-item">Medical<br>Acupuncture</li>
      <li class="service-item">IV<br>Vitamins</li>
      <li class="service-item">Holistic<br>Health.</li>
    </ul>
    <svg class="hill" viewBox="0 0 220 221" aria-hidden="true">
      <path d="M0 221 L0 204 Q100 176 220 172 L220 221 Z" fill="var(--sage-hill)"/>
    </svg>
  </section>

  <section class="window-panel panel-accent">
    <ul class="service-list">
      <li class="service-item">Direct<br>Primary Care</li>
      <li class="service-item">Holistic<br>Medicine</li>
    </ul>
    <p class="web-address">fernbrookcare-example.com</p>
    <svg class="hill" viewBox="0 0 220 221" aria-hidden="true">
      <path d="M0 221 L0 172 Q120 176 220 204 L220 221 Z" fill="var(--sage-hill)"/>
    </svg>
  </section>
</main>
</body>
</html>
```